Fertility Book Cover

This is a book about infertility, treatment options and solutions. The book title is "No caminho do amanhecer". The book is in portuguese, but I believe that won't be a problem to design the cover. I need front and back covers design.
The author name, that should be in book is "Dra. Beatriz Morano Vasconti Telhado".

Letter case could be "No Caminho do Amanhecer"

This is the cover I created, but I don't like it: http://www.docuvelo.com/doc/583190462/27390518-cover

8.5" x 11"

Target Market(s)

Woman and Couples that desire kids and have problem about fertility

Colors
b768aa
e34196
6b449a

Requirements
Nice to have
• a link to our domain: www.ninhoclaro.org (not essential)
More happy images than sad woman...

```html
<!DOCTYPE html>
<html lang="pt">
<head>
<meta charset="utf-8">
<title>No Caminho do Amanhecer — capa</title>
<link rel="stylesheet" href="https://fonts.googleapis.com/css2?family=Josefin+Sans:wght@300&family=Roboto+Condensed:wght@400;500;700&display=swap">
<style>
  :root {
    --magenta: #e0419a;
    --orchid: #b768aa;
    --violet: #6b449a;
    --white: #ffffff;
    --photo-light: #f6e3e6;
    --photo-mid: #dcb3a4;
    --photo-deep: #a97a6a;
  }
  * { margin: 0; padding: 0; box-sizing: border-box; }
  html, body { width: 1200px; height: 776px; overflow: hidden; background: var(--white); }
  .cover { position: relative; width: 1200px; height: 776px; overflow: hidden; }

  .back-cover { position: absolute; left: 0; top: 0; width: 600px; height: 776px; background: var(--magenta); }
  .blurb-panel {
    position: absolute; left: 102px; top: 55px; width: 460px; height: 560px;
    background: var(--orchid); padding: 37px 24px 0 24px; color: var(--white);
    font-family: "Roboto Condensed", "Arial Narrow", sans-serif;
  }
  .epigraph { text-align: right; font-size: 8.5px; line-height: 12px; font-weight: 400; }
  .blurb {
    margin-top: 48px; font-size: 12.4px; line-height: 16.4px; font-weight: 500;
    text-align: justify; letter-spacing: 0;
  }

  .front-cover { position: absolute; left: 600px; top: 0; width: 600px; height: 776px; background: var(--white); }
  .cover-photo {
    position: absolute; left: 0; top: 0; width: 600px; height: 560px;
    background: radial-gradient(ellipse at 55% 55%, var(--photo-mid) 0%, var(--photo-deep) 45%, var(--photo-light) 100%);
  }
  .title-band {
    position: absolute; left: 0; top: 560px; width: 600px; height: 75px;
    background: var(--magenta); color: var(--white);
    font-family: "Josefin Sans", sans-serif; font-weight: 300; font-size: 45px;
    display: flex; align-items: center; justify-content: center; padding-top: 6px; letter-spacing: 0.5px;
  }
  .title-rule { position: absolute; left: 0; top: 639px; width: 600px; height: 4px; background: var(--magenta); }
  .author {
    position: absolute; left: 0; top: 740px; width: 600px; text-align: center;
    font-family: "Roboto Condensed", "Arial Narrow", sans-serif; font-weight: 700; font-size: 15px;
    color: var(--violet);
  }
</style>
</head>
<body>
<main class="cover">
  <section class="back-cover">
    <div class="blurb-panel">
      <p class="epigraph">Quem tem um pão e troca por outro, fica com um pão.<br>Quem tem uma idéia e a troca por outra, fica com duas idéias.<br>Provérbio árabe</p>
      <p class="blurb">A busca pela fertilidade é um processo com várias etapas, desde a identificação do problema até sua resolução. A compreensão é essencial e ocorre logo depois ou concomitante à aceitação. Nesse momento o casal passa a entender a função existencial do ser humano. Ao definir suas prioridades o casal está apto à proceder com os passos seguintes. A fase da compreensão varia muito, podendo ser suficiente apenas uma conversa no consultório com um profissional, ou necessário a opinião de diversos profissionais; assim como também tem aqueles que precisam fazer uma ampla pesquisa na Internet, procuram entrevistas, vídeos e muito mais. O mundo globalizado de hoje oferece a possibilidade de diversas fontes de informação e isso é muito saudável. Entretanto, por outro lado, também se faz necessário uma fonte coerente, concisa, atualizada e confiável, exatamente o que este livro se propõe a fazer. Lembrando que o conhecimento do limite da ciência é muito importante para evitar abusos e sofrimentos desnecessários este livro almeja ser o guia ilustrado e explicado da fertilidade humana, respondendo o que, o como, o quando, o quem, o onde e o porque, de maneira compreensível e com o aprofundamento necessário para elucidar as dúvidas mais frequentes sobre esse assunto. A ciência tem que ser reconhecida pela sua transitoriedade que confere um caráter de mudanças contínuas, ou seja, o que é verdade hoje pode não ser amanhã. Mas, para aqueles que estão em busca de sua fertilidade, a verdade de hoje é a necessária, a de amanhã cabe aos especialistas. Apresentamos aqui a verdade atual sobre a fertilidade.</p>
    </div>
  </section>
  <section class="front-cover">
    <div class="cover-photo" role="img" aria-label="Fotografia de um casal sorridente olhando juntos um teste de gravidez"></div>
    <h1 class="title-band">No Caminho do Amanhecer</h1>
    <div class="title-rule"></div>
    <p class="author">Dra. Beatriz Morano Vasconti Telhado</p>
  </section>
</main>
</body>
</html>
```